Plantwise Mechanics Partners. Needs a Business Card Design

We need a business card design for an engineering company which supplies industrial components (pumps, compressors, mechanical seals) provides repairs and services for above mentioned equipments. We offer a uniqe engineering solutions which help our customers to increase the productivness of their manufacturings, and energy savings.

Target Market(s)

Chemical and energy plants, refineries. Food industry and private consumers in a less.

Industry/Entity Type

Business

Contact Information for Business Card

Stylish and sleek design oriented on industrial area.

Requirements
Should not have
• company name shortening

```html
<!DOCTYPE html>
<html lang="en">
<head>
<meta charset="utf-8">
<title>Plantwise Mechanics Partners – Business Card</title>
<link rel="stylesheet" href="https://fonts.googleapis.com/css2?family=Ubuntu:wght@400;500;700&family=Open+Sans:wght@400;600&display=swap">
<style>
  :root {
    --stage: #2a2a2c;
    --card-white: #ffffff;
    --brand-pink: #ef3f5e;
    --brand-pink-light: #f35a74;
    --brand-blue: #1d49a6;
    --brand-orange: #f6a629;
    --ink-grey: #6d6f73;
    --rule-grey: #d4d6d9;
  }
  * { box-sizing: border-box; margin: 0; padding: 0; }
  html, body { width: 1200px; height: 950px; overflow: hidden; }
  body {
    background: var(--stage);
    font-family: "Open Sans", Arial, sans-serif;
    position: relative;
  }
  .card {
    position: absolute;
    left: 250px;
    width: 700px;
    height: 400px;
    overflow: hidden;
    box-shadow: 0 18px 40px rgba(0,0,0,.45);
  }

  /* Back side */
  .card-back {
    top: 40px;
    background: linear-gradient(135deg, var(--brand-pink-light), var(--brand-pink));
    color: var(--card-white);
    text-align: center;
  }
  .card-back .brand-dot {
    width: 96px; height: 96px; border-radius: 50%;
    background: var(--card-white);
    margin: 92px auto 22px;
  }
  .card-back .brand-name {
    font-family: "Ubuntu", Arial, sans-serif;
    font-weight: 500;
    font-size: 26px;
  }
  .card-back .web-address {
    margin-top: 56px;
    font-family: "Ubuntu", Arial, sans-serif;
    font-size: 17px;
    letter-spacing: 5px;
  }

  /* Front side */
  .card-front {
    top: 510px;
    background: var(--card-white);
  }
  .brand-block {
    position: absolute;
    left: 36px; top: 150px;
    width: 350px;
    text-align: center;
  }
  .brand-block .brand-dot {
    width: 46px; height: 46px; border-radius: 50%;
    background: var(--brand-pink);
    margin: 0 auto 14px;
  }
  .brand-block .brand-name {
    font-family: "Ubuntu", Arial, sans-serif;
    font-weight: 500;
    font-size: 24px;
    color: var(--brand-blue);
    white-space: nowrap;
  }
  .divider {
    position: absolute;
    left: 405px; top: 70px;
    width: 1px; height: 200px;
    background: var(--rule-grey);
  }
  .contact-block {
    position: absolute;
    left: 432px; top: 70px;
    color: var(--ink-grey);
    font-size: 14px;
    line-height: 1.4;
  }
  .contact-block .person-name {
    font-family: "Ubuntu", Arial, sans-serif;
    font-weight: 700;
    font-size: 22px;
    color: var(--brand-blue);
    letter-spacing: .5px;
  }
  .contact-block .person-role {
    font-weight: 600;
    font-size: 12px;
    color: #44464a;
    margin-bottom: 14px;
  }
  .contact-block .address { margin-bottom: 12px; }
  .contact-list { list-style: none; }
  .contact-list li { display: flex; align-items: center; gap: 8px; height: 20px; }
  .contact-list svg { width: 13px; height: 13px; fill: var(--brand-blue); flex: none; }
  .accent-strip {
    position: absolute; left: 0; bottom: 0;
    width: 100%; height: 12px; display: flex;
  }
  .accent-strip span:nth-child(1) { flex: 40; background: var(--brand-blue); }
  .accent-strip span:nth-child(2) { flex: 36; background: var(--brand-pink); }
  .accent-strip span:nth-child(3) { flex: 24; background: var(--brand-orange); }
</style>
</head>
<body>

<section class="card card-back">
  <div class="brand-dot"></div>
  <div class="brand-name">Plantwise Mechanics Partners</div>
  <div class="web-address">WWW.PLANTWISEMP.COM</div>
</section>

<section class="card card-front">
  <div class="brand-block">
    <div class="brand-dot"></div>
    <div class="brand-name">Plantwise Mechanics Partners</div>
  </div>

  <div class="divider"></div>

  <div class="contact-block">
    <div class="person-name">MAREK DOLAN</div>
    <div class="person-role">PRESIDENT</div>
    <div class="address">1270 Harbor Crest Road<br>Millbrook, NY 12545</div>
    <ul class="contact-list">
      <li>
        <svg viewBox="0 0 16 16"><path d="M3.5 1l3 3-1.7 1.8a9 9 0 0 0 5.4 5.4L12 9.5l3 3-2 2.2C7 14.5 1.5 9 1.3 3z"/></svg>
        555 0142 7781
      </li>
      <li>
        <svg viewBox="0 0 16 16"><path d="M4.5 0h7A1.5 1.5 0 0 1 13 1.5v13a1.5 1.5 0 0 1-1.5 1.5h-7A1.5 1.5 0 0 1 3 14.5v-13A1.5 1.5 0 0 1 4.5 0zM5 2v10h6V2zm3 11a1 1 0 1 0 0 2 1 1 0 0 0 0-2z"/></svg>
        555 0198 3364
      </li>
      <li>
        <svg viewBox="0 0 16 16"><path d="M1 3h14v1.2L8 9 1 4.2zM1 5.8l7 4.8 7-4.8V13H1z"/></svg>
        marek@plantwisemp.com
      </li>
      <li>
        <svg viewBox="0 0 16 16"><path d="M8 0a8 8 0 1 0 0 16A8 8 0 0 0 8 0zm5.9 7H11a12 12 0 0 0-1.2-5A6 6 0 0 1 13.9 7zM8 2c.8 1 1.4 2.9 1.5 5h-3C6.6 4.9 7.2 3 8 2zM6.2 2A12 12 0 0 0 5 7H2.1A6 6 0 0 1 6.2 2zM2.1 9H5a12 12 0 0 0 1.2 5A6 6 0 0 1 2.1 9zM8 14c-.8-1-1.4-2.9-1.5-5h3c-.1 2.1-.7 4-1.5 5zm1.8 0A12 12 0 0 0 11 9h2.9a6 6 0 0 1-4.1 5z"/></svg>
        www.plantwisemp.com
      </li>
    </ul>
  </div>

  <div class="accent-strip"><span></span><span></span><span></span></div>
</section>

</body>
</html>
```